Steelcrest Process Systems. Needs a Business Card Design

We need a business card design for an engineering company which supplies industrial components (pumps, compressors, mechanical seals) provides repairs and services for above mentioned equipments. We offer a uniqe engineering solutions which help our customers to increase the productivness of their manufacturings, and energy savings.

Target Market(s)

Chemical and energy plants, refineries. Food industry and private consumers in a less.

Industry/Entity Type

Business

Contact Information for Business Card

Stylish and sleek design oriented on industrial area.

Requirements
Should not have
• company name shortening

```html
<!DOCTYPE html>
<html lang="en">
<head>
<meta charset="utf-8">
<title>Steelcrest Process Systems – Business Card</title>
<link rel="stylesheet" href="https://fonts.googleapis.com/css2?family=Source+Sans+3:wght@400;600;700&family=Ubuntu:wght@500&display=swap">
<style>
  :root {
    --stage: #000000;
    --card: #333438;
    --card-edge: #3a3b40;
    --text: #ffffff;
    --muted: #e6e6e6;
    --orange: #f7a82a;
    --red: #ec4336;
    --blue: #24409a;
    --divider: #4a4b50;
  }
  * { margin: 0; padding: 0; box-sizing: border-box; }
  html, body {
    width: 1200px; height: 900px; overflow: hidden;
    background: var(--stage);
    font-family: "Source Sans 3", "Myriad Pro", sans-serif;
  }
  .canvas { position: relative; width: 1200px; height: 900px; }
  .card {
    position: absolute; top: 271px;
    width: 457px; height: 281px;
    background: var(--card);
    border-radius: 14px;
    box-shadow: inset 0 0 0 1px var(--card-edge);
  }
  .card--front { left: 137px; }
  .card--back { left: 626px; }

  /* front */
  .brand-mark {
    position: absolute; left: 58px; top: 62px; width: 152px;
    display: flex; flex-direction: column; align-items: center; gap: 10px;
  }
  .brand-mark__dot { width: 72px; height: 72px; border-radius: 50%; background: var(--orange); }
  .brand-mark__name {
    color: var(--text); font-size: 15px; font-weight: 600;
    text-align: center; line-height: 1.15;
  }
  .divider {
    position: absolute; left: 224px; top: 78px; width: 1px; height: 142px;
    background: var(--divider);
  }
  .person { position: absolute; left: 240px; top: 54px; }
  .person__name { font-size: 20px; font-weight: 400; line-height: 24px; }
  .person__first { color: var(--orange); }
  .person__last { color: var(--red); }
  .person__role { color: var(--text); font-size: 13px; line-height: 16px; }
  .address {
    position: absolute; left: 239px; top: 113px;
    color: var(--text); font-size: 13px; line-height: 14.5px; font-style: normal;
  }
  .contacts {
    position: absolute; left: 239px; top: 153px; list-style: none;
  }
  .contacts li {
    display: flex; align-items: center; gap: 8px;
    color: var(--text); font-size: 13px; height: 19px;
  }
  .contacts svg { width: 10px; height: 10px; fill: var(--orange); flex: none; }

  /* back */
  .back-mark {
    position: absolute; left: 189px; top: 80px;
    width: 80px; height: 80px; border-radius: 50%; background: var(--orange);
  }
  .company {
    position: absolute; left: 0; right: 0; top: 170px;
    text-align: center; color: var(--text);
    font-family: "Ubuntu", sans-serif; font-weight: 500; font-size: 25px;
  }
  .tagline {
    position: absolute; left: 0; right: 0; top: 216px;
    text-align: center; font-size: 12.5px; font-weight: 700;
  }
  .tagline__lead { color: var(--orange); }
  .tagline__items { color: var(--red); }
</style>
</head>
<body>
<main class="canvas">
  <section class="card card--front">
    <div class="brand-mark">
      <span class="brand-mark__dot"></span>
      <span class="brand-mark__name">Steelcrest Process Systems</span>
    </div>
    <span class="divider"></span>
    <div class="person">
      <p class="person__name"><span class="person__first">Marcus</span> <span class="person__last">Hale</span></p>
      <p class="person__role">Managing Director</p>
    </div>
    <address class="address">4810 Foundry Road<br>Riverton, 204518</address>
    <ul class="contacts">
      <li><svg viewBox="0 0 10 10"><path d="M2 0.5 L3.6 2.6 L2.8 3.6 Q4 6 6.4 7.2 L7.4 6.4 L9.5 8 L8.4 9.5 Q3.5 9 0.5 1.6 Z"/></svg>(044)-318-2265</li>
      <li><svg viewBox="0 0 10 10"><path d="M2.5 0 H7.5 V10 H2.5 Z M3.4 1 V8 H6.6 V1 Z"/></svg>(044)-318-2265</li>
      <li><svg viewBox="0 0 10 10"><path d="M0.5 2 H9.5 V8.5 H0.5 Z M1.5 3 L5 5.6 L8.5 3 Z"/></svg>info@steelcrest-ps.com</li>
      <li><svg viewBox="0 0 10 10"><circle cx="5" cy="5" r="4.6"/></svg>www.steelcrest-ps.com</li>
    </ul>
  </section>

  <section class="card card--back">
    <span class="back-mark"></span>
    <h1 class="company">Steelcrest Process Systems</h1>
    <p class="tagline"><span class="tagline__lead">Repairs and services for pumps,</span> <span class="tagline__items">compressors, mechanical seals</span></p>
  </section>
</main>
</body>
</html>
```